URGENT website build for kids rugby company

We have created a new company that has venues all over London coaching kids age 2-7 fun rugby based activities. This is an urgent job that needs to be finished within 3 weeks.

We need a website built within the next 2-3 weeks that shows all our venues and details of each with a dedicated page that would have a location map, times or lessons, coach profiles and a "book here" button. The site must enable clients to book their "free trial" or "term membership" on the website. This will mean working with our payment company call Tallow Pay, and a CRM booking management site (to be confirmed on Monday 25th Nov). We must have the ability to create a new venue page at any time.

The front page would have a slide show of editable pictures, an intro text area under the picture frame. It would need to have a number of promo boxes on it as well.

It would have a few other pages of info such as:
A page explaining in detail our age groups of which there are 3 (red, green and blue)
how the lessons work and activity examples
terms and conditions
kit you can buy

I will give a more detailed brief on conversation with applicants for the job

It needs to be a kid AND mum friendly design. with easy and familiar usability and as uncluttered as possible. Corporate colours are red, black and white.

Industry/Entity Type

It Company

Requirements
Nice to have
• These are website designs I like and would aspire to have a similar feel to:
• http://www.brovilta-studio.com/
• http://www.quintarmolde.com/
• http://www.zelbrook.com
Should not have
• Site similar to our company include the following - but we do NOT want to look like these but the site content is relevant:
• http://www.ovenpipsters.co.uk/
• http://www.flimtoads.com/
• http://www.gramwickhoppers.com/site/

```html
<!DOCTYPE html>
<html lang="en">
<head>
<meta charset="utf-8">
<title>Company Name – Kids Rugby</title>
<link rel="stylesheet" href="https://fonts.googleapis.com/css2?family=Bebas+Neue&family=Noto+Sans:wght@400;700&display=swap">
<style>
:root{
  --red:#c40000;
  --red-1:#c60000;
  --red-2:#dc0000;
  --red-3:#f40000;
  --red-4:#ff2222;
  --red-deep:#8e0000;
  --footer-text:#4a0000;
  --black:#000;
  --white:#fff;
  --grey:#e8e8e8;
  --text:#222;
  --head:"Bebas Neue",Impact,sans-serif;
  --body:"Noto Sans",Tahoma,sans-serif;
}
*{margin:0;padding:0;box-sizing:border-box}
html,body{width:1013px;height:1200px;overflow:hidden}
body{position:relative;background:var(--white);font-family:var(--body);color:var(--text)}
.abs{position:absolute}

.topbar{left:0;top:0;width:1013px;height:24px;background:var(--red);color:var(--white);font-size:9.5px;line-height:24px}
.topbar .quick{left:95px;top:0}
.topbar .quick span{margin:0 4px}
.topbar .contact{left:518px;top:0;display:flex;align-items:center;gap:6px}
.topbar .contact svg{display:block}
.topbar .sep{margin:0 6px;opacity:.8}
.social{display:flex;gap:10px;margin-left:4px}
.social i{display:block;width:12px;height:12px;border-radius:50%;background:var(--white)}

.header{left:0;top:24px;width:1013px;height:115px;background:linear-gradient(#fff,#ececec)}
.brand{left:93px;top:32px;font-family:var(--head);font-size:50px;line-height:50px;color:var(--red);letter-spacing:.5px}
.nav{left:379px;top:43px;display:flex;align-items:center;font-size:11px;color:#333;height:29px}
.nav a{color:inherit;text-decoration:none;padding:0 14px;border-left:1px solid #999;line-height:16px}
.nav a.home{background:#dcdcdc;width:78px;text-align:center;line-height:29px;border:0;margin-right:13px;padding:0}

.hero{left:0;top:139px;width:1013px;height:386px;background:linear-gradient(180deg,#6e8a55 0%,#58773f 45%,#3f5a2c 100%)}
.arrow{top:272px;width:39px;height:39px;background:rgba(0,0,0,.55);display:flex;align-items:center;justify-content:center}

.intro{left:83px;top:452px;width:847px}
.intro h1{background:var(--red);border:1px solid #fff;height:48px;line-height:52px;text-align:center;color:var(--white);font-family:var(--head);font-weight:400;font-size:28px}
.intro p{background:var(--grey);height:79px;padding:17px 30px 0;text-align:center;font-size:10.4px;line-height:12.2px}

.promos{left:83px;top:579px;width:847px;height:199px;display:flex}
.promo{flex:1;padding:9px 12px 0 14px;color:var(--white)}
.promo:nth-child(1){background:var(--red-1)}
.promo:nth-child(2){background:var(--red-2)}
.promo:nth-child(3){background:var(--red-3)}
.promo:nth-child(4){background:var(--red-4)}
.promo .num{font-family:var(--head);font-size:40px;line-height:38px;display:inline-block;border-bottom:3px solid var(--white)}
.promo h2{font-family:var(--head);font-weight:400;font-size:26px;margin-top:15px;line-height:26px}
.promo p{font-size:10.2px;line-height:12px;margin-top:8px;height:48px;letter-spacing:-.1px}
.btn-more{display:inline-block;margin-top:17px;background:var(--white);color:var(--red);font-family:var(--head);font-size:12.5px;line-height:19px;padding:0 6px}

.col h2{font-family:var(--head);font-weight:400;font-size:24px;color:var(--black);line-height:24px}
.col p{font-size:9.3px;line-height:12.2px;margin-top:11px;color:var(--text)}
.welcome{left:97px;top:795px;width:292px}
.who{left:419px;top:795px;width:275px}
.btn-dark{display:inline-block;margin-top:28px;background:var(--black);color:var(--white);font-family:var(--head);font-size:14px;line-height:22px;padding:0 10px}

.sidebar{left:718px;top:795px;width:212px}
.sidebar a{display:block;height:40px;margin-bottom:2px;background:var(--red);border-left:9px solid var(--red-deep);color:var(--white);text-decoration:none;font-family:var(--head);font-size:22px;line-height:44px;padding-left:18px}
.sidebar a.book{background:var(--black);border-left-color:var(--red)}

.copy{left:0;top:977px;width:1013px;height:38px;background:var(--black);color:var(--white);font-size:9.6px;line-height:38px;text-align:center}

.footer{left:0;top:1015px;width:1013px;height:185px;background:var(--red);color:var(--footer-text)}
.footer h3{font-family:var(--head);font-weight:400;font-size:25px;color:var(--black);line-height:26px}
.footer ul{list-style:none;margin-top:4px}
.footer li{font-size:9.6px;line-height:18.6px;color:var(--footer-text)}
.footer p{font-size:9.4px;line-height:12.4px}
.f-links{left:97px;top:32px}
.f-post{left:235px;top:32px;width:272px}
.f-post p{margin-top:5px}
.f-post p+p{margin-top:7px;padding-left:3px}
.f-gallery{left:536px;top:32px}
.thumbs{display:grid;grid-template-columns:repeat(4,46px);gap:8px 8px;margin-top:2px}
.thumbs div{width:46px;height:46px;background:linear-gradient(160deg,#5e8a4a,#2f4f2a);border:1px solid #fff}
.f-contact{left:777px;top:32px;width:200px}
.f-contact p{margin-top:5px}
.f-contact p+p{margin-top:6px}
.f-contact .mail{text-decoration:underline}
</style>
</head>
<body>

<div class="abs topbar">
  <div class="abs quick">Location Map<span>|</span>Times or Lessons<span>|</span>Coach Profiles</div>
  <div class="abs contact">
    <svg width="11" height="8" viewBox="0 0 11 8"><rect x="0.5" y="0.5" width="10" height="7" fill="none" stroke="#fff"/><path d="M0.5 0.5 L5.5 4.5 L10.5 0.5" fill="none" stroke="#fff"/></svg>
    <span>info@companyname.com</span><span class="sep">|</span>
    <svg width="9" height="9" viewBox="0 0 10 10"><path d="M2 0.5 L4 3 L3 4.2 Q4.5 6.5 5.8 7 L7 6 L9.5 8 L8 9.5 Q3 9 0.5 2 Z" fill="#fff"/></svg>
    <span>123-456-7891</span><span class="sep">|</span>
    <div class="social"><i></i><i></i><i></i><i></i><i></i><i></i></div>
  </div>
</div>

<div class="abs header">
  <div class="abs brand">COMPANY NAME</div>
  <nav class="abs nav">
    <a class="home" href="#">HOME</a>
    <a href="#">ABOUT US</a>
    <a href="#">TERMS AND CONDITIONS</a>
    <a href="#">KIT YOU CAN BUY</a>
    <a href="#">CONTACT US</a>
  </nav>
</div>

<div class="abs hero" role="img" aria-label="Slideshow photo of young children running with a rugby ball on a grass pitch"></div>
<div class="abs arrow" style="left:15px"><svg width="18" height="22" viewBox="0 0 18 22"><path d="M14 2 L5 11 L14 20" fill="none" stroke="#bbb" stroke-width="4"/></svg></div>
<div class="abs arrow" style="left:960px"><svg width="18" height="22" viewBox="0 0 18 22"><path d="M4 2 L13 11 L4 20" fill="none" stroke="#bbb" stroke-width="4"/></svg></div>

<section class="abs intro">
  <h1>COMPANY INTRO MESSAGE...</h1>
  <p>Lorem ipsum dolor sit amet, consectetur adipiscing elit. Cras malesuada, mauris id aliquet congue, nisi velit tempor nisi, nec luctus massa dui non lacus. Mauris vel rutrum mi. Praesent eget nunc in elit venenatis tempor. congue at metus. Curabitur ac massa enim. Curabitur ullamcorper tincidunt ultricies. Phasellus tempus a augue sed semper. In hac habitasse platea dictumst. Curabitur nec est sit amet sem dignissim feugiat a et nulla. Fusce in odio tellus.</p>
</section>

<section class="abs promos">
  <div class="promo"><span class="num">01</span><h2>HEADING HERE...</h2><p>Lorem ipsum dolor sit amet, con-sectetur adipiscing elit. Cras male-suada, mauris id aliquet congue, nisi velit tempor nisi, nec luctus</p><span class="btn-more">READ MORE</span></div>
  <div class="promo"><span class="num">02</span><h2>HEADING HERE...</h2><p>Lorem ipsum dolor sit amet, con-sectetur adipiscing elit. Cras male-suada, mauris id aliquet congue, nisi velit tempor nisi, nec luctus</p><span class="btn-more">READ MORE</span></div>
  <div class="promo"><span class="num">03</span><h2>HEADING HERE...</h2><p>Lorem ipsum dolor sit amet, con-sectetur adipiscing elit. Cras male-suada, mauris id aliquet congue, nisi velit tempor nisi, nec luctus</p><span class="btn-more">READ MORE</span></div>
  <div class="promo"><span class="num">04</span><h2>HEADING HERE...</h2><p>Lorem ipsum dolor sit amet, con-sectetur adipiscing elit. Cras male-suada, mauris id aliquet congue, nisi velit tempor nisi, nec luctus</p><span class="btn-more">READ MORE</span></div>
</section>

<section class="abs col welcome">
  <h2>WELCOME TO SOCCER WORLD</h2>
  <p>Lorem ipsum dolor sit amet, consectetur adipisicing elit, sed do eiusmod tempor incididunt ut labore et dolore magna aliqua. Ut enim ad minim veniam, quis nostrud exercitation ullamco laboris nisi ut aliquip fugiat nulla pariatur. Excepteur sint occaecat cupidatat non proident, sunt in culpa qui officia deserunt mollit anim id est laborum.Sed ut perspiciatis unde omnis iste natus error sit voluptatem accusantium doloremque laudantium, totam rem aperiam, eaque ipsa quae ab illo inventore veritatis et quasi architecto beatae vitae dicta sunt explicabo.</p>
</section>

<section class="abs col who">
  <h2>WHO WE ARE</h2>
  <p>Lorem ipsum dolor sit amet, consectetur adipisicing elit, sed do eiusmod tempor incididunt ut labore et dolore magna aliqua.Ut enim ad minim veniam, quis nostrud exercitation ullamco laboris nisi ut aliquip fugiat nulla pariatur. Excepteur sint occaecat cupidatat non proident, sunt in culpa qui officia deserunt mollit anim id est laborum.</p>
  <span class="btn-dark">READ MORE</span>
</section>

<nav class="abs sidebar">
  <a class="book" href="#">BOOK HERE</a>
  <a href="#">RECENT EVENTS</a>
  <a href="#">OUR COACHES</a>
  <a href="#">TOURS</a>
</nav>

<div class="abs copy">© 2013 COMPANYNAME. ALL RIGHTS RESERVED.</div>

<footer class="abs footer">
  <div class="abs f-links">
    <h3>LINKS</h3>
    <ul><li>Home</li><li>About Us</li><li>Gallery</li><li>Services</li><li>training</li><li>Contact</li></ul>
  </div>
  <div class="abs f-post">
    <h3>LATEST POST</h3>
    <p>Lorem ipsum dolor sit amet, consectetur adipisicing elit, sed do eiusmod tempor incididunt ut labore et dolore magna aliqua. Ut enim ad minim veniam, quis nostrud exercitation ullamco laboris nisi ut aliquip fugiat nulla pariatur. Excepteur sint occaecat cupidatat non.</p>
    <p>proident, sunt in culpa qui officia deserunt mollit anim id est laborum.Sed ut perspiciatis unde omnis iste natus error</p>
  </div>
  <div class="abs f-gallery">
    <h3>GALLERY</h3>
    <div class="thumbs">
      <div role="img" aria-label="Gallery photo of children playing rugby"></div>
      <div role="img" aria-label="Gallery photo of a tackle during a kids match"></div>
      <div role="img" aria-label="Gallery photo of players in red kit"></div>
      <div role="img" aria-label="Gallery photo of a child holding a rugby ball"></div>
      <div role="img" aria-label="Gallery photo of a young player running"></div>
      <div role="img" aria-label="Gallery photo of a player in blue kit"></div>
      <div role="img" aria-label="Gallery photo of a team huddle"></div>
      <div role="img" aria-label="Gallery photo of a child with a ball"></div>
    </div>
  </div>
  <div class="abs f-contact">
    <h3>CONTACT INFO</h3>
    <p>Kite Hollow<br>PO Box 40562<br>Marrow Lane, Fennick<br>Dorland 3094 USA</p>
    <p>Phone: (123) 456-7890<br>Fax: (123) 456-7890</p>
    <p class="mail">support@pellwinfield.com</p>
  </div>
</footer>

</body>
</html>
```